TAVRO Capital Group LLC a High Risk Big Rewards company for Rich Young Entrepreneurs

We would like a very modern, powerful in the eyes of our customers, modern, minimalist feel, financial gain. this business card is for young Rich entrepreneurs who want to invest money into High Risk, Big Rewards Businesses. The card Should sell the business!! let your creativity go Wild! I pick most of the designers for this project because of your BOLD Designs, I would like this card to be Bold, Modern, Minimalist, use as many effects in your graphic Artist Mind, Do not let the Financial sound of this business to make you think Conservative that's the last thing we are! if you have a lot of money and you want to play a risky market call US
Updates

Project Deadline Extended
Reason: have not received, enough designs to choose 1st and second place, sure I have received over 100 designs but it seems most designers are submitting every card they have ever made before and calling it mine, please we are looking for fresh ideas please!

Target Market(s)

Private Risky Investors

Industry/Entity Type

Financial

Contact Information for Business Card

powerful in the eyes of our customers,modern, minimalist feel

Font styles to use
Other font styles liked:
• Modern feeling fonts

Requirements
Must have
• The Company Name is TAVRO Capital Group LLC and it must be on the CARD
• My Name, title, Cell , email
• Delvin Ashcroft G.E.D.
• Managing Member
• 555.038.6195
• delvin@tavrocapitalgroup.example
Nice to have
• try a black thick plastic card with round corners with Delvin Ashcroft GED (make sure GED is smaller than name) just on one side of the card, and my phone number with out the icons and email on the other side, this card should look like a exclusive credit card or exclusive VIP card, something you would never loose

```html
<!DOCTYPE html>
<html lang="en">
<head>
<meta charset="utf-8">
<title>TAVRO Capital Group LLC – Business Card</title>
<link href="https://fonts.googleapis.com/css2?family=Montserrat:wght@400;500;600&display=swap" rel="stylesheet">
<style>
  :root {
    --backdrop: #3b3532;
    --card-black: #0d0d0d;
    --card-glow: #1d1d1d;
    --ink-white: #ffffff;
    --ink-grey: #cfcfcf;
    --accent-red: #e3262b;
    --rule: #555555;
    --silver: #c8c8c8;
  }
  * { margin: 0; padding: 0; box-sizing: border-box; }
  html, body {
    width: 1200px; height: 844px; overflow: hidden;
    background: var(--backdrop);
    font-family: "Montserrat", "Century Gothic", sans-serif;
  }
  .stage {
    width: 1200px; height: 844px;
    display: flex; align-items: center; justify-content: center; gap: 56px;
  }
  .card {
    position: relative; width: 520px; height: 300px;
    background: radial-gradient(ellipse at 50% 35%, var(--card-glow), var(--card-black) 75%);
    box-shadow: 0 16px 34px rgba(0,0,0,.55);
    color: var(--ink-white);
    text-align: center;
    overflow: hidden;
  }
  .brand { font-weight: 500; letter-spacing: .5px; }
  .brand-name { display: block; font-size: 42px; line-height: 1.05; }
  .brand-sub { display: block; font-size: 28px; line-height: 1.15; }
  .brand-mark {
    display: inline-block; width: 14px; height: 14px; border-radius: 50%;
    background: var(--ink-white); margin-right: 10px; vertical-align: middle;
  }

  /* Front */
  .card-front .brand {
    position: absolute; top: 26px; left: 0; right: 0; color: var(--ink-white);
  }
  .rule {
    position: absolute; left: 0; right: 0; height: 1px;
    background: linear-gradient(90deg, transparent, var(--rule) 15%, var(--rule) 85%, transparent);
  }
  .rule-top { top: 168px; }
  .rule-bottom { top: 220px; }
  .holder { position: absolute; top: 120px; left: 0; right: 0; }
  .holder-name { font-size: 21px; font-weight: 600; color: var(--accent-red); }
  .holder-name .credential { font-size: 15px; }
  .holder-title { font-size: 13px; font-weight: 400; color: var(--ink-grey); margin-top: 1px; }
  .contact {
    position: absolute; left: 0; right: 0; font-size: 14px; font-weight: 500;
    color: var(--ink-white);
    display: flex; align-items: center; justify-content: center; gap: 8px;
  }
  .contact-phone { top: 184px; }
  .contact-email { top: 240px; }
  .contact svg { fill: var(--accent-red); flex: none; }

  /* Back */
  .card-back .brand {
    position: absolute; top: 50%; left: 0; right: 0; transform: translateY(-50%);
    color: var(--silver);
  }
  .card-back .brand-name { font-size: 46px; }
  .card-back .brand-sub { font-size: 30px; }
</style>
</head>
<body>
<main class="stage">
  <section class="card card-front" aria-label="Card front">
    <div class="brand">
      <span class="brand-name"><span class="brand-mark"></span>TAVRO</span>
      <span class="brand-sub">Capital Group LLC</span>
    </div>
    <div class="holder">
      <p class="holder-name">Delvin Ashcroft <span class="credential">G.E.D.</span></p>
      <p class="holder-title">Managing Member</p>
    </div>
    <div class="rule rule-top"></div>
    <p class="contact contact-phone">
      <svg width="12" height="12" viewBox="0 0 24 24" aria-hidden="true"><path d="M6.6 10.8a15 15 0 0 0 6.6 6.6l2.2-2.2c.3-.3.7-.4 1-.2 1.1.4 2.3.6 3.6.6.6 0 1 .4 1 1V20c0 .6-.4 1-1 1A17 17 0 0 1 3 4c0-.6.4-1 1-1h3.5c.6 0 1 .4 1 1 0 1.3.2 2.5.6 3.6.1.3 0 .7-.2 1z"/></svg>
      555.038.6195
    </p>
    <div class="rule rule-bottom"></div>
    <p class="contact contact-email">
      <svg width="13" height="10" viewBox="0 0 24 18" aria-hidden="true"><path d="M0 0h24v18H0z M2 2v.6l10 7 10-7V2z" fill-rule="evenodd"/></svg>
      delvin@tavrocapitalgroup.example
    </p>
  </section>
  <section class="card card-back" aria-label="Card back">
    <div class="brand">
      <span class="brand-name">TAVRO</span>
      <span class="brand-sub">Capital Group LLC</span>
    </div>
  </section>
</main>
</body>
</html>
```